Church Offering Envelope for receive weekly offerings

I need the front of an 6 3/4 envelope designed to be a church offering envelope. Our color palette is CMYK, 1a56b7, e8da7e, 19a3a3, 40c7f1, e7282d.
I need all of the text information carried forward from our old envelope (see attached) but the new style needs to be modern and flat. (Don't want another dove and clouds theme) I need a 1/4 border on all four sides as envelopes cannot be printed full bleed.
Logo is attached
Target Market(s)
Church
Industry/Entity Type
Church
Font styles to use
Sans Serif
Requirements
Must have
- must adhere to the color palette is CMYK, 1a56b7, e8da7e, 19a3a3, 40c7f1, e7282d.
- I need all of the text information carried forward from our old envelope (see attached)

```html
<!DOCTYPE html>
<html lang="en">
<head>
<meta charset="utf-8">
<title>Grace Harbor Ministries – Offering Envelope</title>
<link rel="stylesheet" href="https://fonts.googleapis.com/css2?family=EB+Garamond:wght@400&display=swap">
<style>
  :root {
    --page-bg: #ebebeb;
    --paper: #ffffff;
    --royal-blue: #0d4f9c;
    --frame-blue: #1a56b7;
    --teal: #19a3a3;
    --gold: #e2d078;
    --red: #d9352f;
    --ink: #2b2b2b;
  }
  * { box-sizing: border-box; margin: 0; padding: 0; }
  html, body {
    width: 1200px; height: 907px; overflow: hidden;
    background: var(--page-bg);
    font-family: "EB Garamond", Georgia, serif;
    color: var(--ink);
  }
  .envelope {
    position: absolute; left: 60px; top: 148px;
    width: 1080px; height: 611px;
    background: var(--paper);
  }
  .print-area {
    position: absolute; left: 20px; top: 25px;
    width: 1030px; height: 563px;
    border: 2px solid var(--frame-blue);
    overflow: hidden;
  }
  .wave { position: absolute; left: 0; top: 0; width: 100%; height: 100%; }
  .ministry-name {
    position: absolute; left: 57px; top: 92px;
    font-size: 42px; color: var(--red); letter-spacing: 0.5px;
    white-space: nowrap;
  }
  .verse-box {
    position: absolute; left: 638px; top: 57px;
    width: 343px; height: 108px;
    background: var(--gold); border-radius: 8px;
    display: flex; align-items: center; justify-content: center;
    text-align: center; font-size: 20px; line-height: 1.2;
  }
  .verse-ref {
    position: absolute; right: 52px; top: 172px;
    font-size: 18px;
  }
  .field {
    position: absolute; display: flex; align-items: flex-end;
    font-size: 23px; white-space: nowrap;
  }
  .field .line {
    display: inline-block; border-bottom: 1.5px solid var(--ink);
    height: 1px; margin-left: 6px; margin-bottom: 6px;
  }
  .field-name { left: 56px; top: 234px; }
  .field-name .line { width: 844px; }
  .checkbox {
    width: 29px; height: 29px; border: 2.5px solid var(--ink);
    margin-right: 22px; margin-bottom: 2px;
  }
  .field-tithe { left: 59px; top: 288px; }
  .field-tithe .line { width: 270px; }
  .field-radio { left: 59px; top: 351px; }
  .field-radio .line { width: 252px; }
  .notice {
    position: absolute; right: 42px; top: 446px;
    text-align: right; color: var(--paper);
    font-size: 23px; line-height: 34px;
  }
</style>
</head>
<body>
  <main class="envelope">
    <section class="print-area">
      <svg class="wave" viewBox="0 0 1030 563" preserveAspectRatio="none" aria-hidden="true">
        <path fill="var(--teal)" d="M0,410 C250,452 420,488 620,422 C780,370 920,334 1030,322 L1030,334 C920,348 780,388 620,442 C420,508 230,474 0,444 Z"/>
        <path fill="var(--royal-blue)" d="M0,452 C230,484 420,520 625,455 C780,404 920,358 1030,346 L1030,563 L0,563 Z"/>
      </svg>

      <h1 class="ministry-name">Grace Harbor Ministries</h1>

      <blockquote class="verse-box">"Honour the LORD with thy<br>substance and with the firstfruits<br>of all thine increase"</blockquote>
      <p class="verse-ref">by Prov 3:9</p>

      <div class="field field-name">Name:<span class="line"></span></div>
      <div class="field field-tithe"><span class="checkbox"></span>Tithe/Offering<span class="line"></span></div>
      <div class="field field-radio"><span class="checkbox"></span>Radio/Webcast<span class="line"></span></div>

      <p class="notice">Grace Harbor Ministries<br>does not receive restricted<br>funds in amount less than $10,000</p>
    </section>
  </main>
</body>
</html>
```